New Web Design Project

Number of Pages Required

1 page

Requirements
Must have
• An Overview / Background of the Business & Services(not for profit rescue animal farm)
• The Target Market / Audience you are trying to reach (animal lovers)
• Design Specifics; any preferences or ideas for Style, Colour, Imagery, etc (no preferences)

```html
<!DOCTYPE html>
<html lang="en">
<head>
<meta charset="utf-8">
<title>Cedar Hollow Farms</title>
<link href="https://fonts.googleapis.com/css2?family=Montserrat:wght@400;600;700;800&family=Nunito+Sans:wght@400;600;700&display=swap" rel="stylesheet">
<style>
:root{
  --blue:#1ea4dc;
  --ink:#222;
  --text:#333;
  --muted:#777;
  --topbar:#eeeeee;
  --grey-a:#ebebeb;
  --grey-b:#efefef;
  --grey-c:#e8e8e8;
  --ghost:#d9d9d9;
  --footer:#1f1f1f;
  --white:#fff;
}
*{box-sizing:border-box;margin:0;padding:0}
html,body{width:1200px;height:3822px;overflow:hidden}
body{position:relative;font-family:"Nunito Sans",Arial,sans-serif;color:var(--text);background:var(--white)}
.abs{position:absolute}
.heading{font-family:"Montserrat",Arial,sans-serif;font-weight:700;color:var(--blue);text-transform:uppercase}
.ghost{font-family:"Montserrat",Arial,sans-serif;font-weight:700;color:var(--ghost);text-transform:uppercase;white-space:nowrap}
.btn{position:absolute;background:var(--blue);color:var(--white);font-family:"Montserrat",Arial,sans-serif;font-weight:700;font-size:17px;border-radius:30px;display:flex;align-items:center;justify-content:center;text-transform:uppercase}
.para{font-size:15.5px;line-height:34px;color:var(--text)}

/* top bar */
.topbar{left:0;top:0;width:1200px;height:62px;background:var(--topbar)}
.events-tag{left:104px;top:18px;width:143px;height:32px;background:var(--blue);color:#fff;font-size:13px;font-weight:700;display:flex;align-items:center;justify-content:center}
.countdown{left:258px;top:14px;display:flex;gap:26px;font-size:12px;color:var(--muted);text-align:center;line-height:16px}
.top-contact{left:518px;top:22px;font-size:14px;color:var(--muted);display:flex;gap:24px;align-items:center}
.top-sep{top:0;width:1px;height:62px;background:#d6d6d6}
.top-social{left:970px;top:24px;display:flex;gap:10px}
.dot{width:13px;height:13px;border-radius:50%;background:#555}

/* nav */
.nav{left:0;top:62px;width:1200px;height:110px;background:#fff}
.nav a{position:absolute;top:46px;font-size:15px;color:var(--ink);text-decoration:none}
.brand{left:370px;width:420px;top:38px;text-align:center;font-family:"Montserrat",Arial,sans-serif;font-weight:600;font-size:28px;color:var(--ink);letter-spacing:0.5px;white-space:nowrap}

/* hero */
.hero-photo{left:0;top:172px;width:1200px;height:538px;background:linear-gradient(180deg,#1e3216 0%,#3f5e27 40%,#5d8a34 70%,#3f6b25 100%)}
.hero-title{left:596px;top:318px;font-family:"Montserrat",Arial,sans-serif;font-weight:600;font-size:41px;line-height:58px;color:#fff}
.hero-sub{left:598px;top:432px;font-size:20px;line-height:30px;color:#fff;width:560px}
.call{left:601px;top:512px;width:342px;height:69px;background:var(--blue);border-radius:36px;color:#fff;font-family:"Montserrat",Arial,sans-serif;font-weight:700;font-size:21px;display:flex;align-items:center;gap:22px;padding-left:8px}
.call-icon{width:54px;height:54px;border-radius:50%;background:#fff;display:flex;align-items:center;justify-content:center}

/* what we do */
.what{left:0;top:710px;width:1200px;height:577px;background:var(--grey-a)}
.service{width:306px}
.service-photo{height:140px}
.service-label{height:36px;background:var(--blue);color:#fff;font-family:"Montserrat",Arial,sans-serif;font-weight:700;font-size:16px;display:flex;align-items:center;justify-content:center}

/* sponsor */
.sponsor{left:0;top:1847px;width:1200px;height:571px;background:var(--grey-b)}

/* testimonials */
.testi{left:0;top:2418px;width:1200px;height:443px;background:var(--grey-c)}
.avatar{left:525px;top:2685px;width:92px;height:92px;border-radius:50%;background:linear-gradient(160deg,#8a6a52,#3e2c22)}

/* gallery */
.tile{width:117px;height:117px}

/* newsletter */
.news{left:0;top:3264px;width:1200px;height:321px;background:#ececec}
.email{left:178px;top:3468px;width:696px;height:58px;background:#fff;border:1px solid #d2d2d2;font-size:15px;color:#444;display:flex;align-items:center;padding-left:14px}
.subscribe{left:874px;top:3468px;width:148px;height:58px;background:var(--blue);color:#fff;font-weight:700;font-size:15px;display:flex;align-items:center;justify-content:center}

/* footer */
.footer{left:0;top:3585px;width:1200px;height:237px;background:var(--footer);color:#fff}
.footer-name{left:0;width:1200px;top:3622px;text-align:center;font-family:"Montserrat",Arial,sans-serif;font-weight:600;font-size:46px;letter-spacing:1px;color:#fff}
.footer-social{left:0;width:1200px;top:3690px;display:flex;justify-content:center;gap:10px}
.ring{width:30px;height:30px;border-radius:50%;border:2px solid #fff}
.footer-links{left:0;width:1200px;top:3743px;text-align:center;font-size:15px;font-weight:700;color:#fff;word-spacing:2px}
.footer-links span{margin:0 14px;font-weight:400;color:#aaa}
.copy{left:0;width:1200px;top:3784px;text-align:center;font-size:14px;color:#ccc}
</style>
</head>
<body>

<!-- top bar -->
<div class="abs topbar"></div>
<div class="abs events-tag">Upcoming Events</div>
<div class="abs countdown">
  <div>0<br>days</div><div>17<br>hours</div><div>03<br>minutes</div><div>23<br>Seconds</div>
</div>
<div class="abs top-sep" style="left:494px"></div>
<div class="abs top-contact"><span>✉ info@company.com</span><span>☎ 24/7 Support: 888 888 888</span></div>
<div class="abs top-sep" style="left:950px"></div>
<div class="abs top-social"><div class="dot"></div><div class="dot"></div><div class="dot"></div><div class="dot"></div></div>

<!-- navigation -->
<div class="abs nav">
  <a style="left:110px">Home</a>
  <a style="left:194px">About Us</a>
  <a style="left:302px">Events</a>
  <div class="abs brand">CEDAR HOLLOW FARMS</div>
  <a style="left:802px">Meet Our Animals</a>
  <a style="left:956px">Volunteer</a>
  <a style="left:1054px">Contact</a>
</div>

<!-- hero -->
<div class="abs hero-photo" role="img" aria-label="Deer grazing on a green pasture beside a wooden fence in a forest"></div>
<svg class="abs" style="left:0;top:650px" width="1200" height="60" viewBox="0 0 1200 60">
  <path d="M0 60 L520 60 C580 60 600 10 660 10 C720 10 740 60 800 60 L1200 60 Z" fill="var(--grey-a)"/>
</svg>
<div class="abs hero-title">LOVE ANIMALS<br>LIVE COMPASSIONATELY</div>
<div class="abs hero-sub">Sed ut perspiciatis unde omnis iste natus error sit voluptatem accusantium doloremque</div>
<div class="abs call">
  <div class="call-icon">
    <svg width="26" height="26" viewBox="0 0 24 24"><path d="M6.6 10.8c1.4 2.8 3.8 5.1 6.6 6.6l2.2-2.2c.3-.3.7-.4 1-.2 1.1.4 2.3.6 3.6.6.6 0 1 .4 1 1V20c0 .6-.4 1-1 1C10.6 21 3 13.4 3 4c0-.6.4-1 1-1h3.5c.6 0 1 .4 1 1 0 1.3.2 2.5.6 3.6.1.3 0 .7-.2 1L6.6 10.8z" fill="var(--blue)"/></svg>
  </div>
  CALL US: 888 888 8888
</div>

<!-- what we do -->
<div class="abs what"></div>
<div class="abs ghost" style="left:432px;top:800px;font-size:46px">WHAT WE DO</div>
<div class="abs heading" style="left:0;width:1200px;text-align:center;top:816px;font-size:30px">What We Do</div>
<div class="abs para" style="left:105px;width:990px;top:872px;text-align:center">Sed ut perspiciatis unde omnis iste natus error sit voluptatem accusantium doloremque laudantium, totam rem aperiam, eaque ipsa quae ab illo inventore veritatis et quasi architecto beatae vitae dicta sunt explicabo. Nemo enim ipsam voluptatem quia voluptas sit aspernatur aut odit aut fugit, sed quia consequuntur magni dolores eos qui ratione voluptatem sequi nesciunt.</div>
<div class="abs service" style="left:110px;top:1001px">
  <div class="service-photo" role="img" aria-label="Two white horses standing together in a paddock" style="background:linear-gradient(180deg,#5a4a3a,#a39a8c)"></div>
  <div class="service-label">RESCUE</div>
</div>
<div class="abs service" style="left:446px;top:1001px">
  <div class="service-photo" role="img" aria-label="Farm worker in a cowboy hat caring for a dark horse in a stable" style="background:linear-gradient(180deg,#6b5138,#3a2a1e)"></div>
  <div class="service-label">REHABILITATE</div>
</div>
<div class="abs service" style="left:782px;top:1001px">
  <div class="service-photo" role="img" aria-label="Volunteer hugging a horse outside a barn" style="background:linear-gradient(180deg,#8a6f55,#d3c7b8)"></div>
  <div class="service-label">ADVOCATE</div>
</div>

<!-- about -->
<svg class="abs" style="left:82px;top:1362px" width="412" height="412" viewBox="0 0 412 412">
  <path d="M206 4 A202 202 0 0 0 16 270" fill="none" stroke="var(--blue)" stroke-width="8"/>
  <defs><linearGradient id="sunset" x1="0" y1="0" x2="0" y2="1">
    <stop offset="0" stop-color="#e39a3a"/><stop offset="0.45" stop-color="#b07a2c"/><stop offset="1" stop-color="#4d6a22"/>
  </linearGradient></defs>
  <circle cx="206" cy="206" r="199" fill="url(#sunset)" role="img" aria-label="Flock of sheep grazing in a field at sunset"/>
  <circle cx="210" cy="218" r="26" fill="none" stroke="#fff" stroke-width="3"/>
  <path d="M202 205 L224 218 L202 231 Z" fill="none" stroke="#fff" stroke-width="3"/>
</svg>
<div class="abs ghost" style="left:512px;top:1400px;font-size:46px">ABOUT US</div>
<div class="abs heading" style="left:517px;top:1412px;font-size:30px">About Us</div>
<div class="abs para" style="left:517px;width:593px;top:1466px;text-align:justify;line-height:31.5px">Sed ut perspiciatis unde omnis iste natus error sit voluptatem accusantium doloremque laudantium, totam rem aperiam, eaque ipsa quae ab illo inventore veritatis et quasi architecto beatae vitae dicta sunt explicabo. Nemo enim ipsam voluptatem quia voluptas sit aspernatur aut odit aut fugit, sed quia consequuntur magni dolores eos qui ratione voluptatem sequi nesciunt. Neque porro quisquam est, qui dolorem ipsum quia dolor sit amet</div>
<div class="btn" style="left:517px;top:1682px;width:189px;height:51px">Read More</div>

<!-- sponsor -->
<div class="abs sponsor"></div>
<svg class="abs" style="left:601px;top:1847px" width="599" height="571" viewBox="0 0 599 571" role="img" aria-label="Goats grazing on a sunny meadow under a cloudy sky">
  <defs><linearGradient id="meadow" x1="0" y1="0" x2="0" y2="1">
    <stop offset="0" stop-color="#4f6f96"/><stop offset="0.35" stop-color="#c9c2a8"/><stop offset="0.55" stop-color="#7a8a3a"/><stop offset="1" stop-color="#3f5a1c"/>
  </linearGradient></defs>
  <path d="M0 0 L599 0 L599 571 L14 571 C60 470 50 400 18 320 C-10 240 -6 120 0 0 Z" fill="url(#meadow)"/>
</svg>
<div class="abs ghost" style="left:382px;top:1972px;font-size:46px">ANIMAL</div>
<div class="abs heading" style="left:89px;top:1982px;font-size:30px">Sponsor An Animal</div>
<div class="abs para" style="left:89px;width:475px;top:2024px;text-align:justify;line-height:31.5px">Sed ut perspiciatis unde omnis iste natus error sit voluptatem accusantium doloremque laudantium, totam rem aperiam, eaque ipsa quae ab illo inventore veritatis et quasi architecto beatae vitae dicta sunt explicabo. Nemo enim ipsam voluptatem quia voluptas sit aspernatur aut odit aut fugit, sed quia consequuntur magni dolores eos qui ratione voluptatem sequi nesciunt.</div>
<div class="btn" style="left:92px;top:2235px;width:188px;height:51px">Read More</div>

<!-- testimonials -->
<div class="abs testi"></div>
<div class="abs ghost" style="left:0;width:1200px;text-align:center;top:2490px;font-size:70px">TESTIMONIALS</div>
<div class="abs heading" style="left:0;width:1200px;text-align:center;top:2520px;font-size:30px">Testimonials</div>
<div class="abs" style="left:193px;top:2560px;font-size:44px;color:#555;font-family:Georgia,serif">“</div>
<div class="abs para" style="left:250px;width:710px;top:2575px;text-align:center;line-height:33px">Sed ut perspiciatis unde omnis iste natus error sit voluptatem accusantium doloremque laudantium, totam rem aperiam, eaque ipsa quae ab illo inventore veritatis et quasi architecto beatae vitae dicta sunt explicabo.</div>
<div class="abs" style="left:990px;top:2644px;font-size:44px;color:#555;font-family:Georgia,serif">”</div>
<div class="abs avatar" role="img" aria-label="Portrait photo of the reviewer"></div>
<div class="abs" style="left:652px;top:2712px;font-size:13px;color:#333">- ELIN BRANDVOLD</div>
<div class="abs" style="left:652px;top:2733px;font-size:12px;color:#555">Sed ut perspiciatis</div>

<!-- gallery -->
<div class="abs ghost" style="left:0;width:1200px;text-align:center;top:3090px;font-size:150px;color:#efefef;letter-spacing:10px">PICSTREAM</div>
<div class="abs" style="left:127px;top:2934px;font-family:'Montserrat',Arial,sans-serif;font-weight:700;font-size:26px;color:var(--ink)">#CedarHollowFarms</div>
<div class="abs" style="left:130px;top:2972px;width:68px;height:2px;background:#333"></div>
<div class="abs" style="left:202px;top:2962px;width:240px;font-size:11px;font-weight:700;color:#333;line-height:18px;text-align:right">Become our style icon. Tag us on<br>Picstream or Chirper and get featured</div>
<div class="abs tile" style="left:451px;top:2943px;background:linear-gradient(#8d8f8a,#c8b79a)" role="img" aria-label="Horse and foal in a field"></div>
<div class="abs tile" style="left:576px;top:2943px;background:linear-gradient(#e0a040,#5a7a28)" role="img" aria-label="Sheep at sunrise"></div>
<div class="abs tile" style="left:701px;top:2943px;background:linear-gradient(#5e4a3a,#9c8a74)" role="img" aria-label="Horses in a paddock"></div>
<div class="abs tile" style="left:826px;top:2943px;background:linear-gradient(#6e5a48,#2e241c)" role="img" aria-label="Volunteer with a horse"></div>
<div class="abs tile" style="left:576px;top:3070px;background:linear-gradient(#b65a3e,#6a4a3a)" role="img" aria-label="Child with a goat"></div>
<div class="abs tile" style="left:701px;top:3070px;background:linear-gradient(#9fbf7a,#c9a7a0)" role="img" aria-label="Person feeding a lamb"></div>
<div class="abs tile" style="left:826px;top:3070px;background:linear-gradient(#9aa7b0,#d8d0c0)" role="img" aria-label="Sheep being sheared"></div>
<div class="abs tile" style="left:953px;top:3070px;background:linear-gradient(#d8602a,#7a3c1a)" role="img" aria-label="Cattle at sunset"></div>

<!-- newsletter -->
<div class="abs news"></div>
<div class="abs ghost" style="left:0;width:1200px;text-align:center;top:3322px;font-size:50px">SUBSCRIBE TO OUR NEWSLETTER</div>
<div class="abs heading" style="left:0;width:1200px;text-align:center;top:3335px;font-size:30px">Subscribe To Our Newsletter</div>
<div class="abs para" style="left:240px;width:720px;top:3386px;text-align:center;line-height:32px;font-size:17px">At vero eos et accusamus et iusto odio dignissimos ducimus qui blanditiis praesentium voluptatum deleniti atque corrupti quos dolores</div>
<div class="abs email">Enter Your E-mail Address</div>
<div class="abs subscribe">Subscribe Now</div>

<!-- footer -->
<div class="abs footer"></div>
<div class="abs footer-name">CEDAR HOLLOW FARMS</div>
<div class="abs footer-social"><div class="ring"></div><div class="ring"></div><div class="ring"></div><div class="ring"></div></div>
<div class="abs footer-links">Home<span>|</span>About<span>|</span>Meet Our Animals<span>|</span>Events<span>|</span>Volunteer<span>|</span>Contact Us</div>
<div class="abs copy">© 2019 Company Name &nbsp;All right reserved</div>

</body>
</html>
```